Powerpoint template for Trivia Company

Revamp of our current powerpoint template to make it more professional and fun for the players. Something worthy of a trivia company. Please see logo attached for potential colour - but also open to other ideas.

NO BRANDING REQUIRED (IE: No mention of our company or logo on the template please)

Target Market(s)

Bars/restaurants

Colors
3176b5
00a990

```html
<!DOCTYPE html>
<html lang="en">
<head>
<meta charset="utf-8">
<title>Trivia Night – Presentation Template</title>
<link rel="stylesheet" href="https://fonts.googleapis.com/css2?family=Montserrat:ital,wght@0,400;0,500;0,600;0,700;1,500&display=swap">
<style>
:root{
  --stage-top:#f1f2f4;
  --stage-bottom:#e6e2e1;
  --slide:#33375b;
  --slide-left:#383c62;
  --navy:#1e2b4c;
  --teal:#14b393;
  --white:#ffffff;
  --muted:#c9cbe0;
  --blue:#3176b5;
}
*{box-sizing:border-box;margin:0;padding:0}
html,body{width:1200px;height:3297px;overflow:hidden}
body{
  position:relative;
  font-family:"Montserrat",Arial,sans-serif;
  background:linear-gradient(var(--stage-top) 0,var(--stage-top) 998px,var(--stage-bottom) 998px);
  color:var(--white);
}
.slide{position:absolute;width:537px;height:302px;overflow:hidden;background:var(--slide)}
.footer-brand{position:absolute;left:27px;bottom:6px;font-size:5.5px;font-weight:600;color:var(--muted)}
.page-no{position:absolute;right:27px;bottom:6px;font-size:5.5px;color:var(--muted);padding-left:6px;border-left:1px solid var(--muted)}
.dash{display:block;width:18px;height:3px;background:var(--teal);margin-top:9px}

/* title slide */
.title-slide{background:var(--navy);text-align:center}
.title-slide .photo{position:absolute;inset:0;
  background:radial-gradient(circle at 30% 20%,#d7344c 0,transparent 35%),radial-gradient(circle at 70% 25%,#4860d8 0,transparent 35%),linear-gradient(#5a1f4e 0,#3b2554 45%,var(--navy) 80%)}
.title-slide .title-block{position:absolute;left:0;right:0;top:63%}
.title-slide h1{font-weight:700;color:var(--teal);font-size:1.45em;letter-spacing:-.01em}
.title-slide .sub{font-size:.72em;font-weight:500;margin-top:.2em}
.title-slide .dash{margin:.7em auto .6em;width:1.2em;height:.16em}
.title-slide .date{font-size:.55em;font-weight:500}
.hero{left:220px;top:250px;width:760px;height:428px;font-size:24px;box-shadow:0 20px 50px rgba(30,43,76,.25)}
.thumb{font-size:17px}

/* question slides */
.question .panel-left{position:absolute;left:0;top:0;bottom:0;width:210px;background:var(--slide-left)}
.category{position:absolute;left:27px;top:112px;font-size:20px;font-weight:700;line-height:1.1}
.q-label{position:absolute;left:236px;top:32px;font-size:13px;font-weight:700;color:var(--teal)}
.q-text{position:absolute;left:236px;width:262px;font-size:18px;font-weight:500;line-height:25px;padding-left:31px}
.q-text .open{position:absolute;left:0;top:-4px;font-size:40px;font-weight:700;color:var(--teal);line-height:1}
.q-text .close{font-size:40px;font-weight:700;color:var(--teal);line-height:0;vertical-align:-17px;margin-left:3px}
.q-text em{color:var(--teal);font-style:italic}

/* image slides */
.photo-area{position:absolute;top:0;bottom:0;right:0}
.section-title{position:absolute;left:27px;font-weight:700;line-height:1.12}
.section-title small{display:block;font-size:11px;font-weight:700}

/* list slides */
.list-slide h2{position:absolute;left:27px;top:16px;font-size:14px;font-weight:700;line-height:1.15}
.numbered{position:absolute;left:27px;list-style:none;font-size:11px;font-weight:500}
.numbered li{display:flex;gap:6px;margin-bottom:5.5px;line-height:1.25}
.numbered li span{color:var(--teal);min-width:10px;font-size:9px;padding-top:1px}
.categories{font-size:10.5px}
.categories li{margin-bottom:4.5px}

/* rules */
.rules h2{position:absolute;left:27px;top:26px;font-size:14px;font-weight:700}
.rules ul{position:absolute;left:27px;top:60px;width:480px;list-style:none;font-size:8.4px;line-height:1.3}
.rules li{padding-left:8px;position:relative;margin-bottom:3px}
.rules li::before{content:"";position:absolute;left:0;top:4px;width:3px;height:3px;background:var(--teal);border-radius:50%}
.rules .photo-wash{position:absolute;inset:0;background:radial-gradient(circle at 45% 0,rgba(190,40,100,.35),transparent 55%)}

/* brand answer tiles */
.tiles{position:absolute;left:27px;top:56px;display:grid;grid-template-columns:repeat(5,90px);column-gap:9px;row-gap:20px}
.tile{text-align:center}
.tile .mark{width:90px;height:90px;background:var(--white);border-radius:5px;display:flex;align-items:center;justify-content:center;color:var(--navy);font-size:10.5px;font-weight:700;padding:6px;line-height:1.2}
.tile p{font-size:7.5px;font-weight:500;margin-top:6px;line-height:1.2}
</style>
</head>
<body>

<!-- hero title slide -->
<section class="slide title-slide hero">
  <div class="photo" role="img" aria-label="Photo of a crowd raising drinks under coloured party lights"></div>
  <div class="title-block">
    <h1>Welcome to Trivia Night!</h1>
    <p class="sub">Sub Title Presentation</p>
    <span class="dash"></span>
    <p class="date">March, 2020</p>
  </div>
</section>

<!-- row 1 -->
<section class="slide title-slide thumb" style="left:51px;top:964px">
  <div class="photo" role="img" aria-label="Photo of a crowd raising drinks under coloured party lights"></div>
  <div class="title-block">
    <h1>Welcome to Trivia Night!</h1>
    <p class="sub">Sub Title Presentation</p>
    <span class="dash"></span>
    <p class="date">March, 2020</p>
  </div>
</section>

<section class="slide rules" style="left:615px;top:964px">
  <div class="photo-wash"></div>
  <h2>The Rules</h2>
  <ul>
    <li>Teams may have a maximum of 6 players.</li>
    <li>No outside help (internet, phone, etc.) of any kind, including during breaks! If you are caught, your team will be disqualified.</li>
    <li>The game is comprised of 7 rounds of 10 questions—each round is worth 20 points unless otherwise noted. At the end of each round, teams will exchange answer sheets to be graded. After 7 rounds, there will be a FINAL TRIVIA round where each team may wager up to 20 points on a single question.</li>
    <li>Before the game begins, each team must pick one BONUS category (excluding the Final Trivia round) for which they will be awarded double points.</li>
    <li>In the event of a tie, a tie-breaker question will decide the winner. In the unlikely event that the tied teams each answer the question correctly (closest), the winner shall be the team which hands the correct answer to the Quizmaster the quickest.</li>
    <li>The winning team (defined as 2 or more members on the same team, or 1 member if the winner was an individual) from the previous week shall be assessed a handicap equal to ½ of their winning margin (rounded down).</li>
    <li>The Quizmaster has final say on all rule interpretations and disputes.</li>
  </ul>
  <p class="footer-brand">Trivia Company</p><p class="page-no">2</p>
</section>

<!-- row 2 -->
<section class="slide question" style="left:51px;top:1300px">
  <div class="panel-left"></div>
  <h2 class="category">General<br>Knowledge<span class="dash"></span></h2>
  <p class="q-label">Question #1</p>
  <p class="q-text" style="top:84px"><span class="open">“</span>What men’s evening wear got its name from a park in the Hudson Valley where New York’s elite were known to congregate in the 1890s?<span class="close">”</span></p>
  <p class="footer-brand">Trivia Company</p><p class="page-no">5</p>
</section>

<section class="slide list-slide" style="left:615px;top:1300px">
  <h2>This Quiz Contains<br>The Following Categories:</h2>
  <ol class="numbered categories" style="top:62px;width:245px">
    <li><span>1.</span>General Knowledge</li>
    <li><span>2.</span>One Word Movie Titles</li>
    <li><span>3.</span>Name That Year – 2001-2010 Edition (Each Year is Represented)</li>
    <li><span>4.</span>Picture Round – One Letter Logos – Name the Brand/Company</li>
    <li><span>5.</span>Audio Round – Duets – Name the Song and Both Artists</li>
    <li><span>6.</span>Hey Mom, I Got an “A” in Geography!</li>
    <li><span>7.</span>Mmmmm… Beer</li>
    <li><span>8.</span>Final Trivia Round</li>
    <li><span>9.</span>Tie Breaker Question</li>
  </ol>
  <div class="photo-area" role="img" aria-label="Portrait photo of a woman lit by red and blue neon" style="width:263px;background:linear-gradient(120deg,#c23a55 0,#7a3a78 40%,#2a4d8c 75%,#1a2a55 100%)"></div>
  <p class="footer-brand">Trivia Company</p><p class="page-no">3</p>
</section>

<!-- row 3 -->
<section class="slide" style="left:51px;top:1632px">
  <h2 class="section-title" style="top:128px;font-size:19px">First Category:<small>General Knowledge</small><span class="dash"></span></h2>
  <div class="photo-area" role="img" aria-label="Photo of a concert crowd in blue stage light" style="width:340px;clip-path:polygon(20% 0,100% 0,100% 100%,0 100%);background:linear-gradient(160deg,#3d8fd8 0,#1d5a9e 35%,#0f2a55 70%,#0a1630 100%)"></div>
  <p class="footer-brand">Trivia Company</p>
</section>

<section class="slide question" style="left:615px;top:1632px">
  <div class="panel-left"></div>
  <h2 class="category">General<br>Knowledge<span class="dash"></span></h2>
  <p class="q-label">Question #2</p>
  <p class="q-text" style="top:106px"><span class="open">“</span>In the language of international warfare, what do the letters SAM mean?<span class="close">”</span></p>
  <p class="footer-brand">Trivia Company</p><p class="page-no">6</p>
</section>

<!-- row 4 -->
<section class="slide question" style="left:51px;top:1960px">
  <div class="panel-left"></div>
  <h2 class="category">General<br>Knowledge<span class="dash"></span></h2>
  <p class="q-label">Question #3</p>
  <p class="q-text" style="top:106px"><span class="open">“</span>Who is the eldest of the Marlowe sisters?<span class="close">”</span></p>
  <p class="footer-brand">Trivia Company</p><p class="page-no">7</p>
</section>

<section class="slide question" style="left:615px;top:1960px">
  <div class="panel-left"></div>
  <h2 class="category">General<br>Knowledge<span class="dash"></span></h2>
  <p class="q-label">Question #4</p>
  <p class="q-text" style="top:94px"><span class="open">“</span>The Louisiana Purchase occurred during the administration of which U.S. President?<span class="close">”</span></p>
  <p class="footer-brand">Trivia Company</p><p class="page-no">8</p>
</section>

<!-- row 5 -->
<section class="slide question" style="left:51px;top:2287px">
  <div class="panel-left"></div>
  <h2 class="category">General<br>Knowledge<span class="dash"></span></h2>
  <p class="q-label">Question #5</p>
  <p class="q-text" style="top:88px"><span class="open">“</span>Before getting their own long-running series, <em>The Pickwicks</em> appeared in animated shorts on a variety show starring what British comedienne?<span class="close">”</span></p>
  <p class="footer-brand">Trivia Company</p><p class="page-no">9</p>
</section>

<section class="slide question" style="left:615px;top:2287px">
  <div class="panel-left"></div>
  <h2 class="category">General<br>Knowledge<span class="dash"></span></h2>
  <p class="q-label">Question #6</p>
  <p class="q-text" style="top:116px"><span class="open">“</span>What was the sub-title of the second <em>Rex Ranger</em> movie?<span class="close">”</span></p>
  <p class="footer-brand">Trivia Company</p><p class="page-no">10</p>
</section>

<!-- row 6 -->
<section class="slide" style="left:51px;top:2619px">
  <h2 class="section-title" style="top:106px;font-size:19px">Please Pass<br>Your Answers to a<br>Neighboring Team<span class="dash"></span></h2>
  <div class="photo-area" role="img" aria-label="Photo of a dark bar crowd with a blue-lit stage" style="width:305px;clip-path:polygon(22% 0,100% 0,100% 100%,0 100%);background:linear-gradient(150deg,#1a1f55 0,#2b3fc9 35%,#151a45 65%,#0a0c20 100%)"></div>
  <p class="footer-brand">Trivia Company</p>
</section>

<section class="slide list-slide" style="left:615px;top:2619px">
  <h2>Answers</h2>
  <ol class="numbered" style="top:50px;width:240px">
    <li><span>1.</span>Tuxedo</li>
    <li><span>2.</span>Surface to Air Missile</li>
    <li><span>3.</span>Delphine (born in 1979)</li>
    <li><span>4.</span>Elias Whitmore</li>
    <li><span>5.</span>Tessa Ullworth</li>
    <li><span>6.</span>Trail of the Wild</li>
    <li><span>7.</span>Amira Sandoval</li>
    <li><span>8.</span>The Harbor City Herons</li>
    <li><span>9.</span>Mercury</li>
    <li><span>10.</span>Iceland</li>
  </ol>
  <div class="photo-area" role="img" aria-label="Portrait photo of a woman in warm purple bar light" style="width:263px;background:linear-gradient(160deg,#6d4fa8 0,#8a5a9e 40%,#c07a6a 75%,#3a2a4a 100%)"></div>
  <p class="footer-brand">Trivia Company</p><p class="page-no">12</p>
</section>

<!-- row 7 -->
<section class="slide" style="left:51px;top:2947px">
  <h2 class="section-title" style="top:106px;font-size:19px">Please Pass<br>Your Answers to a<br>Neighboring Team<span class="dash"></span></h2>
  <div class="photo-area" role="img" aria-label="Photo of a dancing crowd under pink and violet club lights" style="width:305px;clip-path:polygon(22% 0,100% 0,100% 100%,0 100%);background:linear-gradient(150deg,#3a3ad0 0,#c0358f 40%,#7a1f6e 70%,#1a0f30 100%)"></div>
  <p class="footer-brand">Trivia Company</p>
</section>

<section class="slide list-slide" style="left:615px;top:2947px">
  <h2>Answers</h2>
  <div class="tiles">
    <div class="tile"><div class="mark">Trackline</div><p>1. Trackline</p></div>
    <div class="tile"><div class="mark">Shopway</div><p>2. Shopway</p></div>
    <div class="tile"><div class="mark">Vectora</div><p>3. Vectora</p></div>
    <div class="tile"><div class="mark">Copyra</div><p>4. Copyra</p></div>
    <div class="tile"><div class="mark">Pinboardly</div><p>5. Pinboardly</p></div>
    <div class="tile"><div class="mark">Hearthside</div><p>6. Hearthside</p></div>
    <div class="tile"><div class="mark">Nightowl Games</div><p>7. Nightowl<br>Games</p></div>
    <div class="tile"><div class="mark">Alpenwell</div><p>8. Alpenwell<br>Insurance</p></div>
    <div class="tile"><div class="mark">Crema Co</div><p>9. Crema Co</p></div>
    <div class="tile"><div class="mark">Courtside</div><p>10. Courtside</p></div>
  </div>
  <p class="footer-brand">Trivia Company</p><p class="page-no">14</p>
</section>

</body>
</html>
```